Dockhavenly is a new company, currently under development opening in June. We store & repair shi

This is our first draft of what we want to present & it is very basic.
Our clients are shipping lines and we would like something with a bit of flair. We had the logo designed so those colours of yellow & grey are non negotiable. We are looking for background colours, heading designs etc to blend in whilst incorporating an image of sustainability, moving forward into the future and offering professional service.

Industry/Entity Type

Shipping

```html
<!DOCTYPE html>
<html lang="en">
<head>
<meta charset="utf-8">
<title>Dockhavenly – Presentation Slides</title>
<link href="https://fonts.googleapis.com/css2?family=Signika:wght@400;600&family=Saira+Semi+Condensed:wght@400;500;600&family=Domine:wght@700&display=swap" rel="stylesheet">
<style>
:root{
  --yellow:#fbbc14;
  --yellow-light:#fdd35f;
  --yellow-pale:#fde6a6;
  --gold:#c99e32;
  --slate:#37474f;
  --grey:#6d6e70;
  --grey-mid:#9a9a9a;
  --paper:#ffffff;
  --paper-grey:#efeeef;
  --stage:#000000;
}
*{margin:0;padding:0;box-sizing:border-box}
html,body{width:1048px;height:1200px;overflow:hidden;background:var(--stage)}
body{position:relative;font-family:"Signika",sans-serif;color:var(--slate)}
.slide{position:absolute;width:498px;height:374px;background:var(--paper);overflow:hidden}
.slide--cover{left:20px;top:21px}
.slide--contents{left:527px;top:21px}
.slide--chart{left:20px;top:411px}
.slide--list{left:529px;top:411px}
.slide--columns{left:17px;top:799px;background:var(--paper-grey)}
.slide--about{left:529px;top:799px}

.footer{position:absolute;left:0;bottom:0;width:100%;height:37px;background:var(--slate);border-top:5px solid var(--yellow);
  display:flex;align-items:center;justify-content:space-between;padding:0 14px 0 15px;color:#fff;font-family:"Saira Semi Condensed",sans-serif;font-size:10px}
.footer .page{font-size:12px;font-weight:600}
.slide--cover .footer{font-family:"Signika",sans-serif;font-size:9.5px;padding:0 9px 0 11px}

.brand{position:absolute;display:flex;align-items:center;gap:4px;font-family:"Saira Semi Condensed",sans-serif;font-weight:600;color:var(--slate)}
.brand .mark{background:var(--yellow)}
.brand--small{right:10px;top:12px;font-size:21px}
.brand--small .mark{width:10px;height:10px}
.brand--rule{border-bottom:2px solid var(--yellow);padding:0 0 4px 6px;right:0;width:158px}

.cover-sky{position:absolute;left:0;top:0;width:100%;height:170px;background:linear-gradient(180deg,#dcdcdc 0%,#f4f4f4 60%,#fff 100%)}
.cover-brand{position:absolute;left:0;top:160px;width:100%;display:flex;justify-content:center;align-items:center;gap:8px;font-family:"Saira Semi Condensed",sans-serif;font-weight:600;font-size:44px;color:var(--slate)}
.cover-brand .mark{width:18px;height:18px;background:var(--yellow)}
.cover-tagline{position:absolute;left:0;top:241px;width:100%;text-align:center;font-weight:600;font-size:19px;line-height:27px;color:var(--slate)}

.title-serif{position:absolute;left:12px;top:13px;font-family:"Domine",serif;font-size:20px;color:var(--slate);letter-spacing:.2px}
.title-serif .accent{color:var(--yellow)}
.title-serif::before{content:"";position:absolute;left:-12px;top:-2px;width:6px;height:33px;background:var(--grey)}
.slide--columns .title-serif::before{background:#000;width:5px}
.slide--about .title-serif::before{background:#e8e8e8}

.title-sans{position:absolute;left:28px;top:14px;font-family:"Saira Semi Condensed",sans-serif;font-size:24px;font-weight:400;color:var(--yellow);letter-spacing:.6px}
.title-sans::before{content:"";position:absolute;left:-28px;top:2px;width:10px;height:30px;background:var(--yellow)}
.title-sans::after{content:"";position:absolute;left:-14px;top:2px;width:7px;height:30px;background:var(--grey)}

.contents{position:absolute;left:12px;top:61px;width:480px;height:260px}
.contents-item{position:absolute;display:flex;align-items:center;gap:10px;font-family:"Saira Semi Condensed",sans-serif;font-size:14px;color:var(--slate)}
.contents-item .num{width:31px;height:30px;background:var(--grey);border-left:3px solid var(--yellow);color:#fff;font-size:17px;display:flex;align-items:center;justify-content:center}

.chart-caption{position:absolute;left:26px;top:56px;font-size:10.5px;color:var(--slate)}
.chart{position:absolute;left:0;top:0}
.chart text{font-family:"Signika",sans-serif;font-size:7.5px;fill:var(--slate)}

.bullets{position:absolute;left:14px;top:70px;list-style:none}
.bullets li{display:flex;align-items:center;gap:6px;height:27.6px;font-family:"Saira Semi Condensed",sans-serif;font-size:14px;color:#111}
.bullets svg{flex:none}

.img-slot{position:absolute;top:63px;width:219px;height:88px;background:#fff;border:1px solid #ddd;border-radius:2px;display:flex;align-items:center;justify-content:center;font-size:8px;color:#c4c4c4}
.col-text{position:absolute;top:162px;width:222px;font-size:7.6px;line-height:15px;color:var(--slate)}
.col-text p+p{margin-top:15px}

.about-panel{position:absolute;left:0;top:57px;width:236px;height:277px;background:var(--yellow)}
.about-panel h2{position:absolute;left:23px;top:80px;font-family:"Saira Semi Condensed",sans-serif;font-weight:500;font-size:27px;color:#fff;letter-spacing:.5px}
.about-panel p{position:absolute;left:23px;top:115px;width:196px;font-family:"Saira Semi Condensed",sans-serif;font-size:10px;line-height:12.5px;color:var(--slate);text-align:justify}
.about-photo{position:absolute;left:236px;top:57px;width:262px;height:277px;background:linear-gradient(160deg,#d9d9d9 0%,#a8a8a8 40%,#5e5e5e 75%,#3c3c3c 100%)}
.about-notch{position:absolute;left:236px;top:182px;width:0;height:0;border-top:12px solid transparent;border-bottom:12px solid transparent;border-left:11px solid var(--yellow)}
</style>
</head>
<body>

<section class="slide slide--cover">
  <div class="cover-sky"></div>
  <div class="cover-brand"><span class="mark"></span>Dockhavenly</div>
  <p class="cover-tagline">There’s a new, exciting Container<br>Park opening in Melbourne</p>
  <footer class="footer"><span>12 Harbour Lane, Portside, 3020</span><span>www.dockhavenly.com.au</span></footer>
</section>

<section class="slide slide--contents">
  <h1 class="title-serif"><span class="accent">PROJECT</span> TITLE HERE</h1>
  <div class="brand brand--small"><span class="mark"></span>Dockhavenly</div>
  <div class="contents">
    <div class="contents-item" style="left:0;top:0"><span class="num">01</span>Slide Title Here</div>
    <div class="contents-item" style="left:0;top:44px"><span class="num">02</span>Slide Title Here</div>
    <div class="contents-item" style="left:0;top:92px"><span class="num">03</span>Slide Title Here</div>
    <div class="contents-item" style="left:0;top:141px"><span class="num">04</span>Slide Title Here</div>
    <div class="contents-item" style="left:0;top:186px"><span class="num">05</span>Slide Title Here</div>
    <div class="contents-item" style="left:242px;top:0"><span class="num">06</span>Slide Title Here</div>
    <div class="contents-item" style="left:242px;top:44px"><span class="num">07</span>Slide Title Here</div>
    <div class="contents-item" style="left:242px;top:92px"><span class="num">08</span>Slide Title Here</div>
    <div class="contents-item" style="left:242px;top:141px"><span class="num">09</span>Slide Title Here</div>
    <div class="contents-item" style="left:242px;top:186px"><span class="num">10</span>Slide Title Here</div>
  </div>
  <footer class="footer"><span>Copyright text here</span><span class="page">1</span></footer>
</section>

<section class="slide slide--chart">
  <h1 class="title-sans">PROJECT TITLE HERE</h1>
  <div class="brand brand--small brand--rule"><span class="mark"></span>Dockhavenly</div>
  <p class="chart-caption">Lorem ipsum dolor sit ipsum Lorem ipsum dolor sit ipsum Lorem ipsum Lorem ipsum</p>
  <svg class="chart" width="498" height="320" viewBox="0 0 498 320" aria-label="Bar chart">
    <line x1="108" y1="99" x2="108" y2="280" stroke="#999" stroke-width="1"/>
    <line x1="108" y1="280" x2="425" y2="280" stroke="#999" stroke-width="1"/>
    <rect x="110" y="222" width="20" height="58" fill="var(--grey-mid)"/>
    <rect x="134" y="175" width="26" height="105" fill="var(--yellow)"/>
    <rect x="167" y="194" width="26" height="86" fill="var(--yellow-light)"/>
    <rect x="198" y="229" width="26" height="51" fill="var(--gold)"/>
    <rect x="230" y="266" width="27" height="14" fill="var(--yellow-pale)"/>
    <rect x="262" y="276" width="31" height="4" fill="var(--grey)"/>
    <rect x="298" y="114" width="25" height="166" fill="var(--yellow)"/>
    <rect x="329" y="264" width="27" height="16" fill="var(--yellow-light)"/>
    <rect x="361" y="273" width="26" height="7" fill="var(--yellow-light)"/>
    <text x="25" y="111">Lorem ipsum text here</text>
    <text x="25" y="140">Lorem ipsum text here</text>
    <text x="25" y="179">Lorem ipsum text here</text>
    <text x="25" y="226">Lorem ipsum text here</text>
    <text x="25" y="281">Lorem ipsum text here</text>
    <text x="108" y="298">Lorem ipsum text here</text>
    <text x="217" y="298">Lorem ipsum text here</text>
    <text x="348" y="298">Lorem ipsum text here</text>
  </svg>
  <footer class="footer"><span>Copyright text here</span><span class="page">1</span></footer>
</section>

<section class="slide slide--list">
  <h1 class="title-sans">PROJECT TITLE HERE</h1>
  <div class="brand brand--small brand--rule"><span class="mark"></span>Dockhavenly</div>
  <ul class="bullets">
    <li><svg width="12" height="12" viewBox="0 0 12 12"><rect width="12" height="12" rx="1" fill="var(--yellow)"/><path d="M4 3l3.5 3L4 9" fill="none" stroke="#fff" stroke-width="1.6"/></svg>Lorem ipsum dolor sit ipsum Lorem ipsum dolor sit ipsum Lorem ipsum</li>
    <li><svg width="12" height="12" viewBox="0 0 12 12"><rect width="12" height="12" rx="1" fill="var(--yellow)"/><path d="M4 3l3.5 3L4 9" fill="none" stroke="#fff" stroke-width="1.6"/></svg>Lorem ipsum dolor sit ipsum Lorem ipsum dolor sit ipsum Lorem ipsum</li>
    <li><svg width="12" height="12" viewBox="0 0 12 12"><rect width="12" height="12" rx="1" fill="var(--yellow)"/><path d="M4 3l3.5 3L4 9" fill="none" stroke="#fff" stroke-width="1.6"/></svg>Lorem ipsum dolor sit ipsum Lorem ipsum dolor sit ipsum Lorem ipsum</li>
    <li><svg width="12" height="12" viewBox="0 0 12 12"><rect width="12" height="12" rx="1" fill="var(--yellow)"/><path d="M4 3l3.5 3L4 9" fill="none" stroke="#fff" stroke-width="1.6"/></svg>Lorem ipsum dolor sit ipsum Lorem ipsum dolor sit ipsum Lorem ipsum</li>
    <li><svg width="12" height="12" viewBox="0 0 12 12"><rect width="12" height="12" rx="1" fill="var(--yellow)"/><path d="M4 3l3.5 3L4 9" fill="none" stroke="#fff" stroke-width="1.6"/></svg>Lorem ipsum dolor sit ipsum Lorem ipsum dolor sit ipsum Lorem ipsum</li>
    <li><svg width="12" height="12" viewBox="0 0 12 12"><rect width="12" height="12" rx="1" fill="var(--yellow)"/><path d="M4 3l3.5 3L4 9" fill="none" stroke="#fff" stroke-width="1.6"/></svg>Lorem ipsum dolor sit ipsum Lorem ipsum dolor sit ipsum Lorem ipsum</li>
    <li><svg width="12" height="12" viewBox="0 0 12 12"><rect width="12" height="12" rx="1" fill="var(--yellow)"/><path d="M4 3l3.5 3L4 9" fill="none" stroke="#fff" stroke-width="1.6"/></svg>Lorem ipsum dolor sit ipsum Lorem ipsum dolor sit ipsum Lorem ipsum</li>
    <li><svg width="12" height="12" viewBox="0 0 12 12"><rect width="12" height="12" rx="1" fill="var(--yellow)"/><path d="M4 3l3.5 3L4 9" fill="none" stroke="#fff" stroke-width="1.6"/></svg>Lorem ipsum dolor sit ipsum Lorem ipsum dolor sit ipsum Lorem ipsum</li>
  </ul>
  <footer class="footer"><span>Copyright text here</span><span class="page">1</span></footer>
</section>

<section class="slide slide--columns">
  <h1 class="title-serif"><span class="accent">PROJECT</span> TITLE HERE</h1>
  <div class="brand brand--small"><span class="mark"></span>Dockhavenly</div>
  <div class="img-slot" style="left:14px">IMG HERE</div>
  <div class="img-slot" style="left:258px">IMG HERE</div>
  <div class="col-text" style="left:14px">
    <p>Lorem ipsum dolor sit ipsum Lorem ipsum dolor sit ipsum Lorem ipsum dolor sit ipsum Lorem ipsum dolor sit ipsum lorem ipsum dolor sit ipsum Lorem ipsum dolor sit ipsum Lorem ipsum dolor sit ipsum</p>
    <p>Lorem ipsum dolor sit ipsum Lorem ipsum dolor sit ipsum Lorem ipsum dolor sit ipsum Lorem ipsum dolor sit ipsum lorem ipsum dolor sit ipsum Lorem ipsum dolor sit ipsum Lorem ipsum dolor sit ipsum Lorem ipsum dolor sit ipsum</p>
  </div>
  <div class="col-text" style="left:258px">
    <p>Lorem ipsum dolor sit ipsum Lorem ipsum dolor sit ipsum Lorem ipsum dolor sit ipsum Lorem ipsum dolor sit ipsum lorem ipsum dolor sit ipsum Lorem ipsum dolor sit ipsum Lorem ipsum dolor sit ipsum</p>
    <p>Lorem ipsum dolor sit ipsum Lorem ipsum dolor sit ipsum Lorem ipsum dolor sit ipsum Lorem ipsum dolor sit ipsum lorem ipsum dolor sit ipsum Lorem ipsum dolor sit ipsum Lorem ipsum dolor sit ipsum Lorem ipsum dolor sit ipsum</p>
  </div>
  <footer class="footer"><span>Copyright text here</span><span class="page">1</span></footer>
</section>

<section class="slide slide--about">
  <h1 class="title-serif"><span class="accent">PROJECT</span> TITLE HERE</h1>
  <div class="brand brand--small"><span class="mark"></span>Dockhavenly</div>
  <div class="about-panel">
    <h2>ABOUT US</h2>
    <p>Lorem ipsum dolor sit Lorem ipsum dolor sit Lorem ipsum dolor sit Lorem ipsum dolor sit Lorem ipsum dolor sit Lorem ipsum dolor sit</p>
  </div>
  <div class="about-photo" role="img" aria-label="Black and white photo of an office interior with desks and a mesh office chair"></div>
  <div class="about-notch"></div>
  <footer class="footer"><span>Copyright text here</span><span class="page">1</span></footer>
</section>

</body>
</html>
```